Member Dashboard needs a facelift

Our company is in the consumer credit industry. We offer a service, and once a person signs up for that service, they become a "Member". As a member, they can sign into our "Member Dashboard". What we are looking for is a facelift to our current "Member Dashboard" pages.

We are looking for a cleaner, more modern design that incorporates the same functionality of the current pages (tabs and charts). The graphics elements, buttons and top navigation menu need updating as well.

We are looking for only the page design "look and Feel" and some new great ideas graphicly. Not looking for an entire site.

Please note that the grey background shown in the screen shots is full browser width.

Thank you.
Updates

Thank you everyone for your designs.  Please make sure all designs are in by the end of day.  We will be selecting the 1st and 2nd design tomorrow AM.

 

Thank you for your partisapation.

 

Target Market(s)

Adults over the age of 18 who pay rent in housing.

Industry/Entity Type

Industry

Requirements
Must have
• We are looking for a professional modern look that keeps with the current structure of the current member dashboard. The pages are 1152px wide.

```html
<!DOCTYPE html>
<html lang="en">
<head>
<meta charset="utf-8">
<title>Member Dashboard</title>
<link href="https://fonts.googleapis.com/css2?family=Source+Sans+3:wght@400;600;700&display=swap" rel="stylesheet">
<style>
:root{
  --bg:#d4d5d7;
  --panel:#e6e7e8;
  --white:#ffffff;
  --ink:#1f1f1f;
  --muted:#3a3a3a;
  --green:#5cb544;
  --green-dark:#3f8f2c;
  --field:#3aa3d4;
  --tab:#e9eaeb;
  --pay:#5cb544;
  --owed:#56c6ea;
  --hist:#f0e11a;
  --types:#c4202b;
  --new:#e0398c;
}
*{box-sizing:border-box;margin:0;padding:0}
html,body{width:951px;height:1200px;overflow:hidden;background:var(--bg)}
body{font-family:"Source Sans 3",sans-serif;color:var(--ink)}
.stage{position:relative;width:1152px;height:1453px;transform:scale(0.8255);transform-origin:0 0;background:var(--bg)}
.abs{position:absolute}
.page-title{left:30px;top:36px;font-size:37px;font-weight:400;letter-spacing:-.3px}
.page-title b{font-weight:700}
.nav-btn{top:118px;width:190px;height:33px;border-radius:3px;background:var(--tab);border:1px solid #c8c9cb;font-size:14px;display:flex;align-items:center;justify-content:center}
.nav-btn.active{background:linear-gradient(#6cc44f,#4ea538);border-color:#3f8f2c}
.tab{top:176px;height:40px;width:133px;background:var(--tab);border-radius:4px 4px 0 0;font-size:14px;display:flex;align-items:center;justify-content:center}
.tab.active{background:var(--white)}
.landlord-panel{left:10px;top:207px;width:664px;height:440px;background:var(--panel);border-radius:6px}
.landlord-card{left:19px;top:215px;width:646px;height:425px;background:var(--white);border-radius:6px}
.section-title{color:var(--green);font-weight:700;font-size:29px}
.body-copy{font-size:13.3px;line-height:16.7px;color:var(--ink)}
.field{font-size:11.5px;color:var(--field)}
.edit-btn{left:76px;top:583px;width:74px;height:24px;border-radius:12px;background:linear-gradient(#6fc955,#4ea538);color:#fff;font-size:14px;display:flex;align-items:center;justify-content:center;gap:6px}
.panel-shadow{height:8px;border-radius:50%;background:radial-gradient(ellipse at center,rgba(0,0,0,.55),rgba(0,0,0,0) 70%)}
.verify-panel{left:706px;top:207px;width:436px;height:340px;background:var(--panel);border-radius:6px}
.verify-card{left:715px;top:214px;width:418px;height:326px;background:var(--white);border-radius:4px}
.verify-tab{left:779px;top:182px;width:289px;height:30px;background:var(--panel);border-radius:4px 4px 0 0;color:var(--green);font-weight:700;font-size:21px;text-align:center;line-height:28px}
.gauge{width:184px;height:120px;border:1px solid #d0d0d0;background:linear-gradient(#fff,#f2f2f2)}
.gauge-label{font-size:13.5px;width:200px;text-align:center}
.alert-text{left:806px;top:575px;font-size:20px;font-weight:700;line-height:24px}
.divider{left:20px;width:1112px;height:1px;background:#c2c3c5}
.factors-title{left:22px;top:694px;font-size:26px;font-weight:700}
.factors-intro{left:22px;top:739px;width:570px;font-size:17px;line-height:21px}
.legend-swatch{left:631px;width:25px;height:25px;border-radius:3px}
.legend-pill{left:665px;width:218px;height:30px;border-radius:10px;font-size:20px;padding-left:10px;line-height:30px}
.legend-copy{left:664px;width:445px;font-size:13px;line-height:16.3px}
.pie-label{font-size:21px;font-weight:700;line-height:26px}
.tip{width:130px}
.tip-head{display:flex;align-items:center;gap:4px;font-size:15px;font-weight:600;height:30px}
.tip-q{font-size:15.5px;font-weight:600;line-height:19px;margin-top:8px;height:62px}
.tip-link{display:block;margin-top:12px;padding-left:25px;color:#3aa3d4;font-size:15px;font-weight:600;text-decoration:underline}
.tip-sep{width:1px;height:150px;background:#c2c3c5;top:1272px}
.cta{left:781px;top:1294px;width:337px;height:108px;background:linear-gradient(#5cb544,#3e9a2b);clip-path:polygon(0 0,100% 0,94% 100%,0 100%);color:#fff;font-size:39px;line-height:40px;padding:10px 0 0 14px}
</style>
</head>
<body>
<main class="stage">

  <h1 class="abs page-title"><b>Member</b> Dashboard</h1>

  <nav>
    <div class="abs nav-btn active" style="left:111px">Member Home</div>
    <div class="abs nav-btn" style="left:363px">Rent Profile</div>
    <div class="abs nav-btn" style="left:615px">Credit summary</div>
    <div class="abs nav-btn" style="left:867px">Frequently Asked Questions</div>
  </nav>

  <div class="abs landlord-panel"></div>
  <div class="abs tab active" style="left:73px">Member Name</div>
  <div class="abs tab" style="left:207px">Rental Address</div>
  <div class="abs tab" style="left:342px">Member Contact</div>
  <div class="abs tab" style="left:476px">Landlord Contact</div>
  <section class="abs landlord-card"></section>
  <h2 class="abs section-title" style="left:55px;top:224px">Landlord Verification Center</h2>
  <p class="abs body-copy" style="left:56px;top:287px;width:560px">One of the most omportandt aspects of the service is our ability to communicate with your landlord or property manager and interface calosely as we gather rent payment data to send on to the credit bureau.</p>
  <p class="abs body-copy" style="left:56px;top:354px;width:560px">The landlord data we have in our database appears below. please click on the “edit” butter to make changes. Remember, though, that this information is critical to our electronic interface with your landlord/property manager. Changes alert us to a possibility that you’ve moved and triggers a verification process that should be avoided unless absolutely necessary.</p>

  <div class="abs field" style="left:75px;top:456px">Landlord / Management:</div>
  <div class="abs field" style="left:270px;top:456px">Complex / Property Name:</div>
  <div class="abs field" style="left:466px;top:456px">Street Address 1:</div>
  <div class="abs field" style="left:75px;top:484px">Street Address 2:</div>
  <div class="abs field" style="left:270px;top:484px">City:</div>
  <div class="abs field" style="left:466px;top:484px">Srate:</div>
  <div class="abs field" style="left:75px;top:513px">Zip Cpde:</div>
  <div class="abs field" style="left:270px;top:513px">LandLord Phone Number:</div>
  <div class="abs field" style="left:466px;top:513px">LandLord Fax Number:</div>
  <div class="abs field" style="left:75px;top:542px">Landlord Email:</div>

  <div class="abs edit-btn">
    <svg width="16" height="16" viewBox="0 0 16 16" aria-hidden="true"><path d="M2 14l1-4 8-8 3 3-8 8z" fill="#2d2d2d"/><path d="M2 14l1-4 3 3z" fill="#f1d39a"/></svg>
    Edit
  </div>
  <div class="abs panel-shadow" style="left:30px;top:648px;width:640px"></div>

  <div class="abs verify-panel"></div>
  <div class="abs verify-tab">Member Verification Center</div>
  <section class="abs verify-card"></section>

  <svg width="0" height="0" style="position:absolute">
    <defs>
      <linearGradient id="gaugeFill" x1="0" x2="1">
        <stop offset="0" stop-color="#c81521"/>
        <stop offset=".3" stop-color="#e63d2d"/>
        <stop offset=".5" stop-color="#f59a3c"/>
        <stop offset=".68" stop-color="#7fd06a"/>
        <stop offset="1" stop-color="#1f9a2b"/>
      </linearGradient>
      <g id="dial">
        <path d="M14 90 A78 78 0 0 1 170 90 Z" fill="url(#gaugeFill)"/>
        <path d="M14 90 A78 78 0 0 1 170 90" fill="none" stroke="#222" stroke-width="1.5"/>
        <line x1="12" y1="90" x2="172" y2="90" stroke="#222" stroke-width="1.5"/>
        <text x="14" y="104" font-size="8.5" font-family="Source Sans 3, sans-serif">Needs Attention</text>
        <text x="170" y="104" font-size="8.5" text-anchor="end" font-family="Source Sans 3, sans-serif">Verified</text>
      </g>
    </defs>
  </svg>

  <div class="abs gauge" style="left:731px;top:226px">
    <svg width="184" height="120" viewBox="0 0 184 120" role="img" aria-label="Member name verification gauge">
      <use href="#dial"/>
      <line x1="90" y1="90" x2="89" y2="30" stroke="#111" stroke-width="3"/>
      <circle cx="90" cy="90" r="7" fill="#111"/><circle cx="90" cy="90" r="3" fill="#777"/>
    </svg>
  </div>
  <div class="abs gauge" style="left:935px;top:226px">
    <svg width="184" height="120" viewBox="0 0 184 120" role="img" aria-label="Rental address verification gauge">
      <use href="#dial"/>
      <line x1="90" y1="90" x2="146" y2="70" stroke="#111" stroke-width="3"/>
      <circle cx="90" cy="90" r="7" fill="#111"/><circle cx="90" cy="90" r="3" fill="#777"/>
    </svg>
  </div>
  <div class="abs gauge" style="left:731px;top:381px">
    <svg width="184" height="120" viewBox="0 0 184 120" role="img" aria-label="Member contact verification gauge">
      <use href="#dial"/>
      <line x1="90" y1="90" x2="146" y2="70" stroke="#111" stroke-width="3"/>
      <circle cx="90" cy="90" r="7" fill="#111"/><circle cx="90" cy="90" r="3" fill="#777"/>
    </svg>
  </div>
  <div class="abs gauge" style="left:936px;top:381px">
    <svg width="184" height="120" viewBox="0 0 184 120" role="img" aria-label="Landlord contact information gauge">
      <use href="#dial"/>
      <line x1="90" y1="90" x2="146" y2="70" stroke="#111" stroke-width="3"/>
      <circle cx="90" cy="90" r="7" fill="#111"/><circle cx="90" cy="90" r="3" fill="#777"/>
    </svg>
  </div>
  <div class="abs gauge-label" style="left:721px;top:348px">Member Nmae Verification</div>
  <div class="abs gauge-label" style="left:933px;top:348px">Rental Address Verification</div>
  <div class="abs gauge-label" style="left:726px;top:503px">Member Contact Verification</div>
  <div class="abs gauge-label" style="left:928px;top:503px">Landlord Contact Information</div>
  <div class="abs panel-shadow" style="left:730px;top:545px;width:400px"></div>

  <svg class="abs" style="left:734px;top:569px" width="64" height="56" viewBox="0 0 64 56" aria-hidden="true">
    <path d="M32 3 L62 53 H2 Z" fill="#f6c51a" stroke="#b98a08" stroke-width="2" stroke-linejoin="round"/>
    <rect x="29" y="18" width="6" height="20" rx="2" fill="#111"/>
    <circle cx="32" cy="45" r="3.5" fill="#111"/>
  </svg>
  <p class="abs alert-text">Some information is still required to<br>validate your membership.</p>

  <div class="abs divider" style="top:667px"></div>

  <h2 class="abs factors-title">The&nbsp; 5 Factors That Determine Your Credit Score:</h2>
  <p class="abs factors-intro">Your credit score is based on a number of key factors. The most significant is your history of making payments on time.</p>

  <svg class="abs" style="left:100px;top:860px" width="420" height="360" viewBox="-210 -150 420 360" role="img" aria-label="Pie chart of credit score factors">
    <g transform="translate(0 38) scale(1 .72)">
      <path d="M0 0 L-29.5 -167.4 A170 170 0 0 1 74.5 -152.8 Z" fill="#8e1219"/>
      <path d="M0 0 L74.5 -152.8 A170 170 0 0 1 79.8 150.1 Z" fill="#2f7a22"/>
      <path d="M0 0 L79.8 150.1 A170 170 0 0 1 -167.4 29.5 Z" fill="#2f8fb3"/>
      <path d="M0 0 L-167.4 29.5 A170 170 0 0 1 -122.3 -118.1 Z" fill="#a59a0c"/>
      <path d="M0 0 L-122.3 -118.1 A170 170 0 0 1 -29.5 -167.4 Z" fill="#a82563"/>
    </g>
    <g transform="scale(1 .72)">
      <path d="M0 0 L-29.5 -167.4 A170 170 0 0 1 74.5 -152.8 Z" fill="var(--types)" stroke="#fff" stroke-width="2"/>
      <path d="M0 0 L74.5 -152.8 A170 170 0 0 1 79.8 150.1 Z" fill="var(--pay)" stroke="#fff" stroke-width="2"/>
      <path d="M0 0 L79.8 150.1 A170 170 0 0 1 -167.4 29.5 Z" fill="var(--owed)" stroke="#fff" stroke-width="2"/>
      <path d="M0 0 L-167.4 29.5 A170 170 0 0 1 -122.3 -118.1 Z" fill="var(--hist)" stroke="#fff" stroke-width="2"/>
      <path d="M0 0 L-122.3 -118.1 A170 170 0 0 1 -29.5 -167.4 Z" fill="var(--new)" stroke="#fff" stroke-width="2"/>
    </g>
    <g font-family="Source Sans 3, sans-serif" font-weight="700" text-anchor="middle">
      <text x="18" y="-72" font-size="22" fill="#111">10%</text>
      <text x="92" y="12" font-size="32" fill="#fff">35%</text>
      <text x="-12" y="88" font-size="23" fill="#111">30%</text>
      <text x="-98" y="36" font-size="23" fill="#111">15%</text>
      <text x="-80" y="-58" font-size="23" fill="#111">10%</text>
    </g>
    <g fill="none" stroke="#fff" stroke-width="1.5">
      <path d="M-103 -100 L-80 -100 L-66 -88"/><circle cx="-66" cy="-88" r="4"/>
      <path d="M30 -124 L30 -140 L40 -140"/><circle cx="30" cy="-124" r="4"/>
      <path d="M38 -10 L58 -30 L75 -30"/><circle cx="38" cy="-10" r="4"/>
      <path d="M-150 48 L-150 25"/><circle cx="-150" cy="48" r="4"/>
      <path d="M-10 105 L-40 85"/><circle cx="-10" cy="105" r="4"/>
    </g>
  </svg>
  <div class="abs pie-label" style="left:259px;top:832px">Types of<br>Credit</div>
  <div class="abs pie-label" style="left:127px;top:869px">New<br>Credit</div>
  <div class="abs pie-label" style="left:481px;top:960px">Payment<br>History</div>
  <div class="abs pie-label" style="left:43px;top:1007px">Credit<br>History</div>
  <div class="abs pie-label" style="left:168px;top:1121px">Amount<br>owed</div>

  <div class="abs legend-swatch" style="top:703px;background:var(--pay)"></div>
  <div class="abs legend-pill" style="top:700px;background:var(--pay)">Payment History (35%)</div>
  <p class="abs legend-copy" style="top:736px">Prospective creditors put most weight on how you’ve made your payments in the past and consider that a clear indication of how you willpay back their loan.</p>

  <div class="abs legend-swatch" style="top:797px;background:var(--owed)"></div>
  <div class="abs legend-pill" style="top:794px;background:var(--owed)">Amount Owed (30%)</div>
  <p class="abs legend-copy" style="top:830px">A close second in importance is the amount you owe. Creditors are cautious not to have their loan be the one that puts you over the top financially.</p>

  <div class="abs legend-swatch" style="top:891px;background:var(--hist)"></div>
  <div class="abs legend-pill" style="top:888px;background:var(--hist)">Credit History (15%)</div>
  <p class="abs legend-copy" style="top:924px">Your&nbsp; history of borrowing is important to prospective new lenders. They look to see whether you’ve used credit wisely in the past - an indication of how you might use it in the future.</p>

  <div class="abs legend-swatch" style="top:985px;background:var(--types)"></div>
  <div class="abs legend-pill" style="top:982px;background:var(--types)">Types of Credit (10%)</div>
  <p class="abs legend-copy" style="top:1019px">The type of credit you use is important. Do you use bank credit lines or payday loans to make it through a month? Is the credit you get difficult or easy to get?</p>

  <div class="abs legend-swatch" style="top:1078px;background:var(--new)"></div>
  <div class="abs legend-pill" style="top:1075px;background:var(--new)">New Credit (10%)</div>
  <p class="abs legend-copy" style="top:1114px">If a prospective new creditor sees that you’ve got a lot of new credit’ it could appear to them that their loan could be in jeopardy.</p>

  <div class="abs divider" style="top:1247px"></div>

  <div class="abs tip" style="left:70px;top:1290px">
    <div class="tip-head" style="padding-left:24px">
      <svg width="24" height="24" viewBox="0 0 24 24" aria-hidden="true"><circle cx="10" cy="9" r="6" fill="#eef3f7" stroke="#9aa3ab" stroke-width="2"/><path d="M14 13l6 7" stroke="#6c737a" stroke-width="3" stroke-linecap="round"/></svg>History</div>
    <p class="tip-q">Have you ever made late payments?</p>
    <a class="tip-link">More info</a>
  </div>
  <div class="abs tip-sep" style="left:192px"></div>
  <div class="abs tip" style="left:208px;top:1290px">
    <div class="tip-head" style="padding-left:6px"><span style="font-size:26px;font-weight:700;color:#555;line-height:1">$</span>&nbsp;Balances</div>
    <p class="tip-q">Do you have high balances?</p>
    <a class="tip-link">More info</a>
  </div>
  <div class="abs tip-sep" style="left:328px"></div>
  <div class="abs tip" style="left:349px;top:1290px">
    <div class="tip-head" style="padding-left:4px">
      <svg width="24" height="24" viewBox="0 0 24 24" aria-hidden="true"><rect x="3" y="16" width="4" height="6" fill="#aaa"/><rect x="9" y="11" width="4" height="11" fill="#999"/><rect x="15" y="5" width="4" height="17" fill="#888"/></svg>&nbsp;Acct. Age</div>
    <p class="tip-q">How old are your credit accounts?</p>
    <a class="tip-link">More info</a>
  </div>
  <div class="abs tip-sep" style="left:470px"></div>
  <div class="abs tip" style="left:490px;top:1290px">
    <div class="tip-head" style="padding-left:8px">
      <svg width="24" height="24" viewBox="0 0 24 24" aria-hidden="true"><path d="M12 2l3 7h7l-6 4.5 2.5 7.5L12 16l-6.5 5L8 13.5 2 9h7z" fill="#b5b8bb"/></svg>&nbsp;New Credit</div>
    <p class="tip-q">Have you opened a new account lately?</p>
    <a class="tip-link">More info</a>
  </div>
  <div class="abs tip-sep" style="left:621px"></div>
  <div class="abs tip" style="left:631px;top:1290px">
    <div class="tip-head" style="padding-left:10px">
      <svg width="26" height="24" viewBox="0 0 26 24" aria-hidden="true"><rect x="2" y="3" width="22" height="19" rx="2" fill="#777"/><rect x="5" y="7" width="16" height="11" fill="#ddd"/><text x="13" y="16" font-size="10" text-anchor="middle" font-weight="700" fill="#555" font-family="Source Sans 3, sans-serif">$</text></svg>&nbsp;Types</div>
    <p class="tip-q">What type of account do you have?</p>
    <a class="tip-link">More info</a>
  </div>

  <div class="abs cta">Continue to your<br>Rent Profile</div>
  <svg class="abs" style="left:1078px;top:1322px" width="60" height="52" viewBox="0 0 60 52" aria-hidden="true">
    <circle cx="30" cy="26" r="24" fill="#d9dadb" stroke="#fff" stroke-width="2"/>
    <path d="M16 12 L30 26 L16 40 M29 12 L43 26 L29 40" fill="none" stroke="#fff" stroke-width="5" stroke-linejoin="round"/>
  </svg>
  <div class="abs panel-shadow" style="left:795px;top:1402px;width:300px"></div>

</main>
</body>
</html>
```